Business Card Design Project

I have established a company called "Tidewell" which is a business specialising in psychotherapy/counselling , predominantly for anxiety & depression.

My name is Mel....hence, the Tidewell link. However, Tidewell was also chosen for its reference to green shoots of growth/recovery.

Tidewell is to be "upmarket" and highly professional. I'm keen for the style and colours to reflect this.....taupe/grey with navy/black script, for example.....NO primary colours.

My name needs to be on the card and my mobile number. Not sure, but suspect it should also have my qualifications ( BA (Psych) & BSc (Hons) Psychology). Mobile number 0463 918 207.

```html
<!DOCTYPE html>
<html lang="en">
<head>
<meta charset="utf-8">
<title>Tidewell — Business Card</title>
<link rel="stylesheet" href="https://fonts.googleapis.com/css2?family=Questrial&display=swap">
<style>
  :root {
    --backdrop: #e6e5e1;
    --card-white: #f6f6f4;
    --taupe: #5f5e55;
    --ink-grey: #55544d;
    --shoot-green: #98a33a;
    --card-w: 900px;
    --card-h: 514px;
  }
  * { margin: 0; padding: 0; box-sizing: border-box; }
  html, body {
    width: 1200px;
    height: 800px;
    overflow: hidden;
    background: var(--backdrop);
  }
  .canvas {
    width: 1200px;
    height: 800px;
    display: flex;
    align-items: center;
    justify-content: center;
  }
  .business-card {
    position: relative;
    width: var(--card-w);
    height: var(--card-h);
    background: var(--card-white);
    overflow: hidden;
    font-family: "Questrial", "Century Gothic", sans-serif;
    color: var(--ink-grey);
    box-shadow: 0 2px 10px rgba(0,0,0,0.08);
  }
  .base-band {
    position: absolute;
    left: 0;
    bottom: 0;
    width: 100%;
    height: 190px;
  }
  .base-band path { fill: var(--taupe); }
  .brand-name {
    position: absolute;
    left: 88px;
    top: 262px;
    font-size: 64px;
    letter-spacing: 1px;
    line-height: 1;
    color: var(--ink-grey);
  }
  .contact-block {
    position: absolute;
    right: 72px;
    top: 128px;
    text-align: right;
  }
  .holder-name {
    font-size: 36px;
    line-height: 1.1;
    letter-spacing: 0.5px;
  }
  .qualifications {
    font-size: 18px;
    margin-top: 4px;
  }
  .contact-lines {
    margin-top: 50px;
    font-size: 20px;
    line-height: 1.45;
  }
  .contact-label { color: var(--shoot-green); }
</style>
</head>
<body>
  <main class="canvas">
    <article class="business-card">
      <svg class="base-band" viewBox="0 0 900 190" preserveAspectRatio="none" aria-hidden="true">
        <path d="M0 120 C 220 70, 420 20, 640 8 L 900 0 L 900 190 L 0 190 Z"/>
      </svg>

      <div class="brand-name">TIDEWELL</div>

      <div class="contact-block">
        <h1 class="holder-name">MEL HARLOW</h1>
        <p class="qualifications">BA &amp; BSc Psychology</p>
        <p class="contact-lines">
          <span class="contact-label">Mobile:</span> 0463 918 207<br>
          <span class="contact-label">E-mail:</span> m.harlow@mailbox.com
        </p>
      </div>
    </article>
  </main>
</body>
</html>
```